Real Estate Business Card

On the front side I want to have my info, my brokerage info.
On the back side I want have my complany’s logo, website and Facebook link. I will provide all this once I select a design.

I would like to see Black background and gold text, Dark Blue and gold text and White and blue text designs

Font styles to use
Sans Serif
Script

```html
<!DOCTYPE html>
<html lang="en">
<head>
<meta charset="utf-8">
<title>Hearthline Real Estate – Business Card</title>
<link rel="stylesheet" href="https://fonts.googleapis.com/css2?family=Cabin:wght@400;600;700&family=Playball&display=swap">
<style>
  :root {
    --backdrop: #e6dcd7;
    --navy: #070c22;
    --gold: #d9ad52;
    --gold-light: #f3d98c;
    --gold-deep: #a9772a;
    --ink: #161616;
    --sans: "Cabin", Arial, sans-serif;
    --script: "Playball", cursive;
  }
  * { margin: 0; padding: 0; box-sizing: border-box; }
  html, body { width: 1200px; height: 600px; overflow: hidden; }
  body { background: var(--backdrop); position: relative; font-family: var(--sans); }

  .card {
    position: absolute;
    top: 168px;
    width: 462px;
    height: 264px;
    background: var(--navy);
    overflow: hidden;
  }
  .card--front { left: 140px; }
  .card--back { left: 653px; }

  .foil {
    background: linear-gradient(125deg, var(--gold-deep) 0%, var(--gold) 22%, var(--gold-light) 45%, var(--gold) 65%, var(--gold-deep) 100%);
  }

  /* Front */
  .front-panel {
    position: absolute;
    left: 0; top: 0;
    width: 197px; height: 264px;
    border-radius: 0 7px 7px 0;
  }
  .holder {
    position: absolute;
    left: 0; top: 96px;
    width: 197px;
    text-align: center;
    color: var(--ink);
  }
  .holder-name {
    font-family: var(--script);
    font-size: 29px;
    line-height: 1;
  }
  .holder-rule {
    width: 132px;
    height: 1.5px;
    margin: 5px auto 5px;
    background: var(--ink);
  }
  .holder-title {
    font-size: 8px;
    font-weight: 700;
    letter-spacing: 0.5px;
  }

  .brand-small {
    position: absolute;
    top: 30px;
    left: 356px;
    width: 100px;
    text-align: center;
    color: var(--gold);
  }
  .brand-small .mark {
    display: block;
    width: 14px; height: 14px;
    margin: 0 auto 3px;
    background: var(--gold);
  }
  .brand-small .name {
    font-size: 8px;
    font-weight: 700;
    letter-spacing: 0.5px;
  }

  .contact {
    position: absolute;
    right: 44px;
    text-align: right;
    color: var(--gold);
    font-size: 8.5px;
    line-height: 11px;
  }
  .contact--phone { top: 104px; font-weight: 600; }
  .contact--mail { top: 137px; }
  .contact--address { top: 161px; }

  .contact-icon {
    position: absolute;
    right: 0;
    width: 25px;
    height: 19px;
    border-radius: 4px 0 0 4px;
    display: flex;
    align-items: center;
    justify-content: center;
  }
  .contact-icon svg { width: 12px; height: 12px; }
  .icon--phone { top: 103px; }
  .icon--mail { top: 132px; }
  .icon--pin { top: 159px; height: 20px; }

  /* Back */
  .edge-strip {
    position: absolute;
    top: 8px;
    width: 12px;
    height: 248px;
  }
  .edge-strip--left { left: 0; border-radius: 0 6px 6px 0; }
  .edge-strip--right { right: 0; border-radius: 6px 0 0 6px; }

  .brand {
    position: absolute;
    left: 0; top: 72px;
    width: 100%;
    text-align: center;
    color: var(--gold);
    font-weight: 700;
  }
  .brand .mark {
    display: block;
    width: 46px; height: 46px;
    margin: 0 auto 12px;
    background: var(--gold);
  }
  .brand .name {
    display: block;
    font-size: 30px;
    line-height: 1;
    letter-spacing: 0.5px;
  }
  .brand .tagline {
    display: block;
    margin-top: 4px;
    font-size: 7.5px;
    letter-spacing: 4px;
  }

  .links {
    position: absolute;
    left: 0; top: 238px;
    width: 100%;
    display: flex;
    justify-content: center;
    gap: 22px;
    color: var(--gold);
    font-size: 8.5px;
  }
  .link { display: flex; align-items: center; gap: 8px; }
  .link svg { width: 15px; height: 15px; }
  .link .dot {
    width: 14px; height: 14px;
    border-radius: 50%;
    background: var(--gold);
  }
</style>
</head>
<body>

<section class="card card--front" aria-label="Business card front">
  <div class="front-panel foil" role="img" aria-label="Gold foil texture panel"></div>
  <div class="holder">
    <p class="holder-name">Dana Whitfield</p>
    <div class="holder-rule"></div>
    <p class="holder-title">BROKER</p>
  </div>

  <div class="brand-small">
    <span class="mark"></span>
    <span class="name">HEARTHLINE</span>
  </div>

  <p class="contact contact--phone">+41555012398<br>+41555046712</p>
  <p class="contact contact--mail">dana.whitfield@hearthline.com</p>
  <p class="contact contact--address">Cedar Road, 45 B<br>City<br>CANADA</p>

  <div class="contact-icon icon--phone foil">
    <svg viewBox="0 0 24 24"><path fill="#070c22" d="M6.6 10.8a15.1 15.1 0 0 0 6.6 6.6l2.2-2.2c.3-.3.7-.4 1-.2 1.1.4 2.3.6 3.6.6.6 0 1 .4 1 1V20c0 .6-.4 1-1 1C10.6 21 3 13.4 3 4c0-.6.4-1 1-1h3.5c.6 0 1 .4 1 1 0 1.3.2 2.5.6 3.6.1.3 0 .7-.2 1z"/></svg>
  </div>
  <div class="contact-icon icon--mail foil">
    <svg viewBox="0 0 24 24"><rect x="2.5" y="5" width="19" height="14" rx="1" fill="none" stroke="#070c22" stroke-width="2"/><path d="M3 6l9 7 9-7" fill="none" stroke="#070c22" stroke-width="2"/></svg>
  </div>
  <div class="contact-icon icon--pin foil">
    <svg viewBox="0 0 24 24"><path fill="#070c22" d="M12 2a7 7 0 0 0-7 7c0 5.2 7 13 7 13s7-7.8 7-13a7 7 0 0 0-7-7zm0 9.5A2.5 2.5 0 1 1 12 6.5a2.5 2.5 0 0 1 0 5z"/></svg>
  </div>
</section>

<section class="card card--back" aria-label="Business card back">
  <div class="edge-strip edge-strip--left foil" role="img" aria-label="Gold foil edge strip"></div>
  <div class="edge-strip edge-strip--right foil" role="img" aria-label="Gold foil edge strip"></div>

  <div class="brand">
    <span class="mark"></span>
    <span class="name">HEARTHLINE</span>
    <span class="tagline">REAL ESTATE</span>
  </div>

  <div class="links">
    <span class="link">
      <svg viewBox="0 0 24 24" fill="none" stroke="#d9ad52" stroke-width="1.6"><circle cx="12" cy="12" r="9.5"/><ellipse cx="12" cy="12" rx="4" ry="9.5"/><path d="M2.5 12h19M4 7h16M4 17h16"/></svg>
      www.hearthline.com
    </span>
    <span class="link">
      <span class="dot"></span>
      www.friendhub.com/hearthline
    </span>
  </div>
</section>

</body>
</html>
```